Rose Confetti Balloons Packaging

We need a packaging design for a 14cm x 20cm plastic bag. The two balloon pictures are going to be in the package. The Fenwold Logo needs to be somewhere small on the lower right. The packaging color should have some rose gold, white, and gold coloring. There will be 10 balloons in the package and there should be "10 Pieces" somewhere on the packaging. The name of the packaging will be "LumeBlooms" somewhere.

Target Market(s)

Weddings, engagements, birthdays, celebrations.

Industry/Entity Type

Plastic

Colors
f68e4e
fee3d5
fabb94
ffffff

Requirements
Must have
• The Fenwold Logo needs to be somewhere small on the lower right. The packaging color should have some rose gold, white, and gold coloring. There will be 10 balloons in the package and there should be "10 Pieces" somewhere on the packaging. The name of the packaging will be "LumeBlooms" somewhere.

```html
<!DOCTYPE html>
<html lang="en">
<head>
<meta charset="utf-8">
<title>LumeBlooms Balloon Packaging</title>
<link rel="stylesheet" href="https://fonts.googleapis.com/css2?family=Didact+Gothic&family=Josefin+Sans:wght@300;600&display=swap">
<style>
  :root {
    --backdrop: #e9ecee;
    --white: #ffffff;
    --peach: #fabb94;
    --peach-soft: #fee3d5;
    --coral: #f68e4e;
    --gold-dark: #7d6b1e;
    --gold-light: #ece07a;
    --rose-dark: #b27a72;
    --rose-light: #f6dcd8;
    --ink: #1b1b1b;
  }
  * { margin: 0; padding: 0; box-sizing: border-box; }
  html, body { width: 1200px; height: 923px; overflow: hidden; }
  body {
    position: relative;
    background: var(--backdrop);
    font-family: "Didact Gothic", "Josefin Sans", sans-serif;
  }
  .pack {
    position: absolute;
    width: 357px;
    height: 509px;
    background: var(--white);
    overflow: hidden;
  }
  .pack--gold { left: 37px; top: 37px; }
  .pack--peach { left: 435px; top: 210px; }
  .pack--rose { left: 822px; top: 384px; }

  .pattern {
    position: absolute;
    inset: 0;
  }
  .pattern--rose {
    background: linear-gradient(160deg, var(--white) 0%, var(--peach-soft) 45%, var(--white) 70%, var(--peach-soft) 100%);
  }
  .pattern--gold {
    background: linear-gradient(160deg, var(--white) 0%, #f6eed0 45%, var(--white) 70%, #f3e8c2 100%);
  }

  .badge {
    position: absolute;
    left: 18px;
    top: 14px;
    width: 65px;
    height: 65px;
    border-radius: 50%;
    color: var(--white);
    display: flex;
    flex-direction: column;
    align-items: center;
    justify-content: center;
    line-height: 1;
  }
  .badge__count { font-family: "Josefin Sans", sans-serif; font-weight: 600; font-size: 36px; margin-top: 6px; }
  .badge__unit { font-size: 11px; letter-spacing: 0.5px; margin-top: -2px; }
  .badge--gold { background: radial-gradient(circle at 60% 40%, var(--gold-light), var(--gold-dark)); }
  .badge--peach { background: var(--peach); }
  .badge--rose { background: radial-gradient(circle at 60% 40%, var(--rose-light), var(--rose-dark)); color: var(--ink); }

  .band {
    position: absolute;
    left: 0;
    right: 0;
    top: 320px;
    height: 92px;
    display: flex;
    align-items: center;
    justify-content: center;
    border-top: 3px solid var(--white);
    border-bottom: 3px solid var(--white);
    box-shadow: 0 -5px 0 -2px var(--peach), 0 5px 0 -2px var(--peach);
  }
  .band--gold { background: linear-gradient(90deg, var(--gold-dark), var(--gold-light) 50%, var(--gold-dark)); }
  .band--peach { background: var(--peach); }
  .band--rose { background: linear-gradient(90deg, var(--rose-dark), var(--rose-light) 55%, var(--rose-dark)); }

  .product-name { font-size: 42px; line-height: 1; }
  .product-name--gold { font-family: "Josefin Sans", sans-serif; font-weight: 600; color: var(--white); }
  .product-name--peach { font-family: "Didact Gothic", sans-serif; color: var(--white); letter-spacing: 1px; }
  .product-name--rose { font-family: "Josefin Sans", sans-serif; font-weight: 300; color: var(--ink); font-size: 36px; letter-spacing: 2px; }

  .maker {
    position: absolute;
    right: 16px;
    bottom: 12px;
    font-family: "Didact Gothic", sans-serif;
    font-size: 16px;
    color: var(--ink);
  }
</style>
</head>
<body>
  <section class="pack pack--gold">
    <div class="pattern pattern--rose" role="img" aria-label="Rose gold line pattern of wedding cakes, champagne glasses, rings, party hats and fireworks"></div>
    <div class="badge badge--gold"><span class="badge__count">10</span><span class="badge__unit">PACK</span></div>
    <div class="band band--gold"><span class="product-name product-name--gold">LumeBlooms</span></div>
    <span class="maker">Fenwold</span>
  </section>

  <section class="pack pack--peach">
    <div class="pattern pattern--gold" role="img" aria-label="Gold foil line pattern of wedding cakes, champagne glasses, rings, party hats and fireworks"></div>
    <div class="badge badge--peach"><span class="badge__count">10</span><span class="badge__unit">PACK</span></div>
    <div class="band band--peach"><span class="product-name product-name--peach">LumeBlooms</span></div>
    <span class="maker">Fenwold</span>
  </section>

  <section class="pack pack--rose">
    <div class="pattern pattern--rose" role="img" aria-label="Rose gold line pattern of wedding cakes, champagne glasses, rings, party hats and fireworks"></div>
    <div class="badge badge--rose"><span class="badge__count">10</span><span class="badge__unit">PACK</span></div>
    <div class="band band--rose"><span class="product-name product-name--rose">LumeBlooms</span></div>
    <span class="maker">Fenwold</span>
  </section>
</body>
</html>
```